Need a book cover design for a Lumora Book on Herbal Remedies

I need a book cover for my new ebook, here are the details:
Title: Meadow Cures
Sub-Heading: Buried Ancient Garden Tonics
Reclaiming the Wisdom of Roots for Everyday Wellness and Strength
Author: Nora Belcourt

```html
<!DOCTYPE html>
<html lang="en">
<head>
<meta charset="utf-8">
<title>Meadow Cures – Book Cover</title>
<link rel="stylesheet" href="https://fonts.googleapis.com/css2?family=DM+Serif+Display&family=Montserrat:wght@400;700&display=swap">
<style>
  :root {
    --page-bg: #ffffff;
    --leaf-deep: #0f2a22;
    --leaf-mid: #1d4a3a;
    --leaf-bright: #1f8f45;
    --cream: #f8f5ec;
    --ink-green: #174a36;
    --tag-text: #e8efe9;
  }
  * { margin: 0; padding: 0; box-sizing: border-box; }
  html, body {
    width: 1200px; height: 1200px; overflow: hidden;
    background: var(--page-bg);
  }
  .cover {
    position: absolute; left: 197px; top: 50px;
    width: 806px; height: 1100px; overflow: hidden;
  }
  .cover-art {
    position: absolute; inset: 0;
    background:
      radial-gradient(circle at 8% 6%, rgba(40,170,80,0.85) 0, rgba(40,170,80,0) 22%),
      radial-gradient(circle at 92% 82%, rgba(40,170,80,0.8) 0, rgba(40,170,80,0) 24%),
      radial-gradient(circle at 55% 45%, var(--leaf-mid) 0, var(--leaf-deep) 80%);
  }
  .title {
    position: absolute; left: 0; right: 0; top: 190px;
    text-align: center; color: var(--cream);
    font-family: "DM Serif Display", serif;
    font-size: 124px; line-height: 1.0; letter-spacing: 1px;
  }
  .subheading {
    position: absolute; left: 62px; width: 682px; top: 508px; height: 66px;
    background: var(--cream); border-radius: 33px;
    display: flex; align-items: center; justify-content: center;
    color: var(--ink-green);
    font-family: "DM Serif Display", serif; font-size: 38px;
  }
  .tagline {
    position: absolute; left: 40px; right: 40px; top: 640px;
    text-align: center; color: var(--tag-text);
    font-family: "Montserrat", sans-serif; font-size: 27px; line-height: 1.4;
  }
  .author-label {
    position: absolute; left: 0; right: 0; top: 790px;
    text-align: center; color: var(--cream);
    font-family: "Montserrat", sans-serif; font-weight: 700; font-size: 24px;
  }
  .author-name {
    position: absolute; left: 240px; width: 326px; top: 822px; height: 66px;
    background: var(--cream); border-radius: 33px;
    display: flex; align-items: center; justify-content: center;
    color: var(--ink-green);
    font-family: "Montserrat", sans-serif; font-weight: 700; font-size: 30px;
  }
</style>
</head>
<body>
  <main class="cover">
    <div class="cover-art" role="img" aria-label="Close-up photograph of dense dark green leaves with bright green blurred leaves in the corners"></div>
    <h1 class="title">Meadow<br>Cures</h1>
    <p class="subheading">Buried Ancient Garden Tonics</p>
    <p class="tagline">Reclaiming the Wisdom of Roots for<br>Everyday Wellness and Strength</p>
    <p class="author-label">Author</p>
    <p class="author-name">Nora Belcourt</p>
  </main>
</body>
</html>
```